Remodeling brochure

We need an informative homeowner friendly brochure detailing our company and things we do. We are looking for an initial setup and ideas (# of pages, etc) and then we will send more content. We are uploading our logo design. We are a high end remodeling company specializing in kitchen & bath remodels. We sell ourselves on customer communication and attention to detail in our designs and remodels.

Target Market(s)

Residential homeowners

Contact Information for Business Card

Modern and attention grabbing

Requirements
Must have
• Name- Hearth & Tile Crafters<br/>Address- 728 NW Folley Lane Suite #217<br/> Brookvale, Kansas 50388<br/>Phone- 555-472-8093<br/>email-htcrafterspro@mailvane.net

```html
<!DOCTYPE html>
<html lang="en">
<head>
<meta charset="utf-8">
<title>Hearth &amp; Tile Crafters – Brochure Spreads</title>
<link rel="stylesheet" href="https://fonts.googleapis.com/css2?family=Lato:ital,wght@0,400;0,700;1,700&family=Ubuntu:wght@400;500&display=swap">
<style>
:root{
  --backdrop:#3a1226;
  --paper:#ffffff;
  --charcoal:#2b2c2d;
  --navy:#1e2a36;
  --blue:#1f6fc2;
  --blue-deep:#1c4fae;
  --blue-bright:#2a8ee0;
  --ink:#2a2a2a;
  --muted:#4a4a4a;
}
*{margin:0;padding:0;box-sizing:border-box}
html,body{width:868px;height:1200px;overflow:hidden;background:var(--backdrop)}
body{position:relative;font-family:"Lato",sans-serif;color:var(--ink)}
h1,h2,h3{font-weight:400}
.abs{position:absolute}
.photo{position:absolute}

/* spread one */
.page-white{background:var(--paper)}
.page-dark{background:var(--charcoal)}
.logo-panel{background:radial-gradient(ellipse at 50% 75%,#5a5b5c 0%,var(--charcoal) 60%)}
.brand{position:absolute;display:flex;align-items:center;gap:8px;color:var(--blue);font-family:"Lato",sans-serif;font-weight:700;text-transform:uppercase;white-space:nowrap}
.brand-mark{background:var(--blue);display:block}
.address{left:67px;width:367px;text-align:center;font-size:9.5px;line-height:11px;color:var(--ink)}
.phone-large{left:67px;width:367px;text-align:center;font-size:19px;color:var(--ink)}
.email-small{left:67px;width:367px;text-align:center;font-size:9.5px;color:var(--ink)}
.contact-band{left:434px;top:542px;width:367px;height:30px;background:linear-gradient(180deg,var(--blue-bright),var(--blue-deep));color:#fff;font-weight:700;font-style:italic;font-size:12.5px;display:flex;align-items:center;justify-content:center}
.accent-line{position:absolute;background:var(--blue-deep)}

/* spread two */
.top-band{left:67px;top:615px;width:734px;height:13px;background:var(--blue-bright)}
.motto{left:103px;font-family:"Ubuntu",sans-serif;font-weight:400;color:var(--blue);line-height:1;letter-spacing:1px}
.section-title{left:102px;font-weight:700;color:#111;text-transform:uppercase}
.rule{left:92px;top:879px;width:187px;height:1px;background:#333}
.body-copy{left:112px;width:282px;text-align:center;font-size:5.6px;line-height:7.3px;color:var(--muted)}
.body-copy p{margin-bottom:4px}
.offers-title{left:593px;top:674px;font-family:"Ubuntu",sans-serif;font-weight:400;font-size:23px;letter-spacing:2px;color:var(--blue)}
.offer{left:593px;display:flex;gap:9px;width:180px}
.offer-mark{width:19px;height:19px;flex:none;background:linear-gradient(90deg,var(--blue-bright),var(--blue-deep))}
.offer h3{font-size:6.6px;font-weight:400;color:#111;margin-top:1px;white-space:nowrap}
.offer p{font-size:4.3px;line-height:6px;color:#222;margin-top:1px}
.overview-heading{left:680px;top:955px;font-family:"Ubuntu",sans-serif;font-weight:400;font-size:11.5px;color:#fff;letter-spacing:.5px}
.overview-label{left:484px;top:972px;font-size:7.5px;color:#fff}
.overview-table{left:475px;top:986px;width:289px;height:75px;border-top:1px solid #888;border-bottom:1px solid #888;display:flex}
.overview-keys{width:157px;background:linear-gradient(180deg,var(--blue-deep),#2553b0);padding:0 9px}
.overview-keys div{height:24px;display:flex;align-items:center;font-size:7px;font-weight:700;color:#fff;border-bottom:1px solid #c9d6ee}
.overview-keys div:last-child{border-bottom:none}
.overview-values{padding:8px 0 0 7px}
.overview-values p{font-size:5px;line-height:7px;color:#fff;height:20px}
.closing-copy{left:506px;top:1074px;width:240px;text-align:center;font-size:5px;line-height:7px;color:#fff}
</style>
</head>
<body>

<!-- spread one: back cover & front cover -->
<section class="spread spread-covers">
  <div class="abs page-white" style="left:67px;top:67px;width:367px;height:518px"></div>
  <div class="abs logo-panel" style="left:148px;top:67px;width:207px;height:408px"></div>
  <div class="photo" role="img" aria-label="Bright white kitchen with island and bar stools" style="left:155px;top:87px;width:193px;height:134px;background:linear-gradient(160deg,#d9c1b8,#ece6df 50%,#c9a56e)"></div>
  <div class="photo" role="img" aria-label="Warm-lit bathroom vanity with vessel sink, granite top and round mirror" style="left:155px;top:238px;width:193px;height:127px;background:linear-gradient(150deg,#8a5a35,#c99a6a 45%,#9a8a80)"></div>
  <div class="brand" style="left:163px;top:412px;font-size:11.5px"><span class="brand-mark" style="width:22px;height:22px"></span>Hearth &amp; Tile Crafters</div>
  <p class="abs address" style="top:494px">728 NW Folley Lane Suite #217<br>Brookvale, Kansas 50388</p>
  <p class="abs phone-large" style="top:526px">555-472-8093</p>
  <p class="abs email-small" style="top:547px">email-htcrafterspro@mailvane.net</p>

  <div class="abs page-dark" style="left:434px;top:67px;width:367px;height:518px;background:radial-gradient(ellipse 45% 22% at 50% 12%,#55575a,var(--charcoal))"></div>
  <div class="brand" style="left:456px;top:110px;font-size:14px"><span class="brand-mark" style="width:28px;height:28px"></span>Hearth &amp; Tile Crafters</div>
  <div class="photo" role="img" aria-label="White farmhouse kitchen with pendant lights and wooden stools" style="left:434px;top:175px;width:223px;height:170px;background:linear-gradient(170deg,#e8ebee,#f4f4f2 55%,#8a7764)"></div>
  <div class="accent-line" style="left:661px;top:175px;width:2px;height:95px"></div>
  <div class="photo" role="img" aria-label="Penny tile wall with chrome faucet" style="left:666px;top:244px;width:125px;height:101px;background:linear-gradient(160deg,#8f9cb8,#b9c1d3)"></div>
  <div class="accent-line" style="left:448px;top:348px;width:127px;height:2px"></div>
  <div class="accent-line" style="left:701px;top:348px;width:80px;height:2px"></div>
  <div class="photo" role="img" aria-label="Double vanity with round mirrors and wall lights" style="left:434px;top:355px;width:149px;height:107px;background:linear-gradient(180deg,#e6e6e6,#cfd0d0 70%,#555)"></div>
  <div class="accent-line" style="left:588px;top:450px;width:2px;height:87px"></div>
  <div class="photo" role="img" aria-label="Travertine bathroom with walk-in shower, toilet and wall sink" style="left:595px;top:355px;width:196px;height:170px;background:linear-gradient(150deg,#d8c3ab,#b79d82 60%,#6a5a4c)"></div>
  <div class="abs contact-band">555-472-8093 | email-htcrafterspro@mailvane.net</div>
</section>

<!-- spread two: inside pages -->
<section class="spread spread-inside">
  <div class="abs page-white" style="left:67px;top:615px;width:734px;height:518px"></div>
  <div class="abs top-band"></div>

  <svg class="abs" style="left:0;top:0" width="868" height="1200" viewBox="0 0 868 1200" aria-hidden="true">
    <defs>
      <linearGradient id="hexFill" x1="0" y1="0" x2="1" y2="0">
        <stop offset="0" stop-color="#2a8ee0"/><stop offset="1" stop-color="#1c4fae"/>
      </linearGradient>
      <linearGradient id="wedgeFill" x1="0" y1="0" x2="1" y2="1">
        <stop offset="0" stop-color="#2a8ee0"/><stop offset="1" stop-color="#1c4fae"/>
      </linearGradient>
    </defs>
    <polygon points="237,707 270,726 270,765 237,784 203,765 203,726" fill="url(#hexFill)"/>
    <polygon points="243,1056 801,815 801,1133 426,1133" fill="#2b2c2d"/>
  </svg>

  <div class="photo" role="img" aria-label="Marble kitchen countertop with cooktop beneath a window" style="left:67px;top:985px;width:359px;height:148px;clip-path:polygon(0 0,176px 71px,359px 148px,0 148px);background:linear-gradient(180deg,#eef0f0,#cfc6b4 55%,#a8987c)"></div>
  <svg class="abs" style="left:67px;top:985px" width="62" height="75" viewBox="0 0 62 75" aria-hidden="true">
    <polygon points="0,0 61,26 0,74" fill="url(#wedgeFill)"/>
  </svg>

  <h1 class="abs motto" style="top:716px;font-size:21px">DREAMS</h1>
  <p class="abs motto" style="top:739px;font-size:13.5px">DON’T WORK</p>
  <p class="abs motto" style="top:756px;font-size:21px">UNLESS</p>
  <p class="abs motto" style="top:778px;font-size:21px">YOU DO !!</p>

  <div class="photo" role="img" aria-label="Hand adjusting a wall-mounted water heater" style="left:262px;top:672px;width:97px;height:89px;background:linear-gradient(160deg,#d8c9c0,#b98d79 60%,#3d74b8)"></div>
  <div class="abs" style="left:364px;top:672px;width:96px;height:89px;background:var(--navy)"></div>
  <div class="photo" role="img" aria-label="Kitchen with dark island and stone floor" style="left:465px;top:672px;width:96px;height:89px;background:linear-gradient(170deg,#b8ab8e,#8c8370 55%,#5b5348)"></div>
  <div class="photo" role="img" aria-label="Hand turning a shower control dial" style="left:262px;top:765px;width:97px;height:89px;background:linear-gradient(150deg,#dfe6ea,#b9c6cd)"></div>
  <div class="photo" role="img" aria-label="Modern bathroom with twin white basins on dark wood" style="left:364px;top:765px;width:96px;height:89px;background:linear-gradient(180deg,#d9d4cc,#5a4535 55%,#3b2e25)"></div>
  <div class="photo" role="img" aria-label="Dark wood bathroom vanity with mirror" style="left:465px;top:765px;width:96px;height:89px;background:linear-gradient(170deg,#9a8877,#4b3b30 60%,#2a221d)"></div>

  <h2 class="abs section-title" style="top:833px;font-size:13px">Brand Positioning</h2>
  <p class="abs section-title" style="top:853px;font-size:10px">Brand Positioning</p>
  <div class="abs rule"></div>
  <div class="abs body-copy" style="top:900px">
    <p>Lorem ipsum dolor sit amet, consectetuer adipiscing elit, sed diam nonummy nibh euismod tincidunt ut laoreet dolore magna aliquam erat volutpat. Ut wisi enim ad minim veniam, quis nostrud exerci tation ullamcorper suscipit lobortis nisl ut aliquip ex ea commodo consequat.</p>
    <p>Duis autem vel eum iriure dolor in hendrerit in vulputate velit esse molestie consequat, vel illum dolore eu feugiat nulla facilisis at vero eros et accumsan et iusto odio dignissim qui blandit praesent luptatum zzril delenit augue duis dolore te feugait nulla facilisi.</p>
    <p>Lorem ipsum dolor sit amet, cons ectetuer adipiscing elit, sed diam nonummy nibh euismod tincidunt ut laoreet dolore magna aliquam erat volutpat. Ut wisi enim ad minim veniam, quis nostrud exerci tation ullamcorper suscipit lobortis nisl ut aliquip ex ea commodo consequat.</p>
  </div>

  <h2 class="abs offers-title">OUR OFFERS</h2>
  <div class="abs offer" style="top:716px"><span class="offer-mark"></span><div><h3>Lorem ipsum dolor sit amet, consectetuer</h3><p>Lorem ipsum dolor sit amet, consectetuer adipiscing elit, sed diam nonummy nibh euismod tincidunt ut laoreet dolore</p></div></div>
  <div class="abs offer" style="top:755px"><span class="offer-mark"></span><div><h3>Lorem ipsum dolor sit amet, consectetuer</h3><p>Lorem ipsum dolor sit amet, consectetuer adipiscing elit, sed diam nonummy nibh euismod tincidunt ut laoreet dolore</p></div></div>
  <div class="abs offer" style="top:792px"><span class="offer-mark"></span><div><h3>Lorem ipsum dolor sit amet, consectetuer</h3><p>Lorem ipsum dolor sit amet, consectetuer adipiscing elit, sed diam nonummy nibh euismod tincidunt ut laoreet dolore</p></div></div>

  <h3 class="abs overview-heading">OUR OFFERS</h3>
  <p class="abs overview-label">OVER VIEW</p>
  <div class="abs overview-table">
    <div class="overview-keys">
      <div>Project Name :</div>
      <div>Client :</div>
      <div>Category :</div>
    </div>
    <div class="overview-values">
      <p>Lorem ipsum dolor sit amet, consectetuer<br>adipiscing elit, sed diam nonummy nibh euismod</p>
      <p>Lorem ipsum dolor sit amet, consectetuer<br>adipiscing elit, sed diam nonummy nibh euismod</p>
      <p>Lorem ipsum dolor sit amet, consectetuer<br>adipiscing elit, sed diam nonummy nibh euismod</p>
    </div>
  </div>
  <p class="abs closing-copy">Lorem ipsum dolor sit amet, consectetuer adipiscing elit, sed diam nonummy nibh euismod tincidunt ut laoreet dolore magna aliquam erat volutpat. Ut wisi enim ad minim veniam, quis nostrud exerci tation ullamcorper suscipit lobortis nisl ut aliquip ex ea commodo consequat. Duis autem vel eum iriure dolor in hendrerit in vulputate velit esse molestie consequat, vel illum</p>
</section>

</body>
</html>
```